Detailing informational flyer

I want to design a new flyer for my automotive detailing business. The flyer should use the color scheme from the logo and be easy to read and understand the services we offer.

Font styles to use
Serif
Sans Serif

Colors
3176b5
0255a3
fbed22
33a6d7
0692cd
ffffff

Requirements
Must have
• must include all information from the copy
Nice to have
• include a Glenvaro logo such as the image attached

```html
<!DOCTYPE html>
<html lang="en">
<head>
<meta charset="utf-8">
<title>Ridgeview Detail Center – Flyer</title>
<link href="https://fonts.googleapis.com/css2?family=Montserrat:wght@400;500;600;700&family=Oswald:wght@500&display=swap" rel="stylesheet">
<style>
:root{
  --navy:#13235a;
  --blue:#0255a3;
  --mid-blue:#3176b5;
  --sky:#33a6d7;
  --aqua:#0692cd;
  --splash:#7fd0f2;
  --yellow:#fbed22;
  --gold:#f1c40f;
  --white:#ffffff;
  --ink:#1d1d28;
  --page:#e9e9ea;
}
*{margin:0;padding:0;box-sizing:border-box}
html,body{width:806px;height:1200px;overflow:hidden;background:var(--page)}
body{font-family:"Montserrat",sans-serif;color:var(--ink);position:relative}
.flyer{position:absolute;top:317px;width:380px;height:566px;background:var(--white);overflow:hidden;box-shadow:0 4px 14px rgba(0,0,0,.18)}
.flyer--front{left:15px}
.flyer--back{left:411px}
.photo{position:absolute;left:0;top:0;width:100%}
.photo--wash{height:290px;background:linear-gradient(160deg,#5d6b76 0%,#2f3a44 45%,#9aa6ad 100%)}
.photo--spray{height:240px;background:linear-gradient(150deg,#7a1010 0%,#c8201c 45%,#3a3f46 100%)}
.wave{position:absolute;left:0;width:100%}
.brand{position:absolute;display:flex;align-items:center;gap:6px}
.brand__dot{width:14px;height:14px;border-radius:50%;background:var(--yellow);flex:none}
.brand__name{font-weight:700;color:var(--navy);font-size:13px;line-height:1.15;letter-spacing:.5px;text-transform:uppercase}
.partner{position:absolute;right:14px;top:345px;font-weight:700;font-size:20px;color:var(--navy);letter-spacing:.5px;text-transform:uppercase}
.pitch{position:absolute;left:0;right:0;top:407px;text-align:center;color:var(--navy);text-transform:uppercase}
.pitch__line{font-size:11.5px;font-weight:400;line-height:17px}
.pitch b{font-weight:700}
.pitch__rule{width:206px;height:1px;background:var(--navy);margin:4px auto 0}
.tab{position:absolute;height:17px;display:flex;align-items:center;padding:0 12px;background:var(--navy);color:var(--white);font-size:8.5px;font-weight:600;text-transform:uppercase}
.tab::after{content:"";position:absolute;right:-9px;top:0;width:0;height:0;border-top:17px solid var(--navy);border-right:9px solid transparent}
.tab__edge{position:absolute;height:17px;width:9px;background:var(--gold);transform:skewX(28deg)}
.copy{position:absolute;font-size:7.6px;line-height:10px}
.copy--center{text-align:center;left:30px;right:30px}
.copy--justify{text-align:justify;left:16px;right:16px}
.footer{position:absolute;left:0;bottom:0;width:100%;height:26px;background:var(--navy);color:var(--white);display:flex;align-items:center;padding:0 14px;font-size:6.5px}
.footer__item{display:flex;align-items:center;gap:4px}
.footer__addr{line-height:8px;text-align:center}
.footer__sep{width:1px;height:14px;background:var(--white);opacity:.6;margin:0 8px}
.footer__phone{margin-left:auto;font-family:"Oswald",sans-serif;font-size:15px;font-weight:500;letter-spacing:.3px}
.footer svg{flex:none}
</style>
</head>
<body>

<!-- Front side -->
<section class="flyer flyer--front">
  <div class="photo photo--wash" role="img" aria-label="Photo of a detailer scrubbing a soapy car wheel with a sponge"></div>
  <svg class="wave" style="top:200px" width="380" height="150" viewBox="0 0 380 150" aria-hidden="true">
    <path d="M0 60 C60 95 110 100 170 92 C230 84 260 40 300 30 C340 20 370 40 380 20 L380 150 L0 150 Z" fill="var(--splash)"/>
    <path d="M0 78 C60 112 120 118 180 108 C240 98 270 60 310 52 C345 45 370 60 380 48 L380 150 L0 150 Z" fill="var(--white)"/>
  </svg>

  <div class="brand" style="left:28px;top:340px">
    <span class="brand__dot"></span>
    <span class="brand__name">Ridgeview<br>Detail Center</span>
  </div>
  <div class="partner">Glenvaro</div>

  <div class="pitch">
    <p class="pitch__line">Ask to speak to a <b>manager</b></p>
    <p class="pitch__line">About <b>scheduling</b> any of our detailing <b>services</b></p>
    <div class="pitch__rule"></div>
  </div>

  <div class="tab__edge" style="left:252px;top:457px"></div>
  <div class="tab" style="left:118px;top:457px">Exterior detailing includes</div>

  <p class="copy copy--center" style="top:485px">We wash, clay, compound, polish, and wax, as needed to restore the deep rich gloss and provide a durable shine for that “new car” look. This process removes light oxidation from the vehicle and protects the clear coat finish. Finishing touches include rim cleaning and tire shine.</p>

  <footer class="footer">
    <span class="footer__item">
      <svg width="7" height="9" viewBox="0 0 10 13"><path d="M5 0C2.2 0 0 2.2 0 5c0 3.5 5 8 5 8s5-4.5 5-8c0-2.8-2.2-5-5-5zm0 7a2 2 0 110-4 2 2 0 010 4z" fill="var(--yellow)"/></svg>
      <span class="footer__addr">48-20 Harbor Ave<br>Elm Gardens</span>
    </span>
    <span class="footer__sep"></span>
    <span class="footer__item">
      <svg width="8" height="8" viewBox="0 0 10 10"><circle cx="5" cy="5" r="5" fill="var(--yellow)"/></svg>
      @ridgeviewcarwash10101
    </span>
    <span class="footer__sep"></span>
    <span class="footer__item footer__phone">
      <svg width="11" height="11" viewBox="0 0 24 24"><path d="M6.6 10.8a15 15 0 006.6 6.6l2.2-2.2a1 1 0 011-.25 11.4 11.4 0 003.6.57 1 1 0 011 1V20a1 1 0 01-1 1A17 17 0 013 4a1 1 0 011-1h3.5a1 1 0 011 1c0 1.25.2 2.45.57 3.57a1 1 0 01-.25 1z" fill="var(--yellow)"/></svg>
      +1 555-014-2290
    </span>
  </footer>
</section>

<!-- Back side -->
<section class="flyer flyer--back">
  <div class="photo photo--spray" role="img" aria-label="Photo of a pressure washer spraying the hood of a red car"></div>
  <svg class="wave" style="top:150px" width="380" height="130" viewBox="0 0 380 130" aria-hidden="true">
    <path d="M0 55 C50 30 90 40 140 70 C200 100 250 85 300 40 C330 15 360 20 380 30 L380 130 L0 130 Z" fill="var(--splash)"/>
    <path d="M0 80 C50 55 100 70 150 92 C210 115 260 100 310 68 C340 50 365 55 380 60 L380 130 L0 130 Z" fill="var(--white)"/>
  </svg>

  <div class="brand" style="left:36px;top:262px">
    <span class="brand__dot"></span>
    <span class="brand__name" style="font-size:11px">Ridgeview<br>Detail Center</span>
  </div>

  <div class="tab__edge" style="left:214px;top:302px"></div>
  <div class="tab" style="left:0;top:302px;padding-left:16px">Interior detailing shampoo includes</div>
  <p class="copy copy--justify" style="top:325px">We perform a deep cleaning of the interior such as the dashboard, door jams, center console, trunk area, upholstered seats, and all carpets and mats. This process will remove soils and most stains. Windows are cleaned inside and out. All leather is dressed to provide a protective finish. Air fresher is available upon request.</p>

  <div class="tab__edge" style="left:165px;top:377px"></div>
  <div class="tab" style="left:0;top:377px;padding-left:16px">Mini detail/ VIP service includes</div>
  <p class="copy copy--justify" style="top:400px">Ridgeview Special Wash with triple polish wax, Glenvaro Shield protectant, tire shine, and a detailed and gentle cleaning of the upholstery. 4 rubber or carpet mats are shampooed. All interior surfaces are dressed including dashboard, door panels, center console. This is followed by a detailed carpet and upholstery vacuum with compressed air to remove dirt from hard to reach places. For added shine ask about adding on our express wax service to your mini detail package.</p>

  <div class="tab__edge" style="left:140px;top:474px"></div>
  <div class="tab" style="left:0;top:474px;padding-left:16px">Headlight restoration</div>
  <p class="copy copy--justify" style="top:497px">This shop proudly offers the Headlight Service, which can polish or restore your headlight to a clear, safe condition at a fraction of the cost of headlight replacement! Restore the lens to a clear, shiny &amp; safe condition.</p>

  <footer class="footer">
    <span class="footer__item">
      <svg width="7" height="9" viewBox="0 0 10 13"><path d="M5 0C2.2 0 0 2.2 0 5c0 3.5 5 8 5 8s5-4.5 5-8c0-2.8-2.2-5-5-5zm0 7a2 2 0 110-4 2 2 0 010 4z" fill="var(--yellow)"/></svg>
      <span class="footer__addr">48-20 Harbor Ave<br>Elm Gardens</span>
    </span>
    <span class="footer__sep"></span>
    <span class="footer__item">
      <svg width="8" height="8" viewBox="0 0 10 10"><circle cx="5" cy="5" r="5" fill="var(--yellow)"/></svg>
      @ridgeviewcarwash10101
    </span>
    <span class="footer__sep"></span>
    <span class="footer__item footer__phone">
      <svg width="11" height="11" viewBox="0 0 24 24"><path d="M6.6 10.8a15 15 0 006.6 6.6l2.2-2.2a1 1 0 011-.25 11.4 11.4 0 003.6.57 1 1 0 011 1V20a1 1 0 01-1 1A17 17 0 013 4a1 1 0 011-1h3.5a1 1 0 011 1c0 1.25.2 2.45.57 3.57a1 1 0 01-.25 1z" fill="var(--yellow)"/></svg>
      +1 555-014-2290
    </span>
  </footer>
</section>

</body>
</html>
```